Custom Cabinet Shop Needs a website design

Hi,
We need a website for a Custom Cabinet Shop and Cabinet parts manufacturing business.
The business has two sides to it. One side provides custom Kitchens, vanities, entertainment units, offices and what not to homeowners and contractors.
The 2nd side of the business provides built to order cabinet boxes and other parts required to put together a project to other cabinet shops, small contractors looking to install there own cabinets.
Website will need a Gallery to display work.
Color scheme to go well with logo.
current website is www.brindlemoorcustomcabinets.com
being changed to www.brindlemoor.ca
Tagline "Joinery with Spirit"
Mission Statement "Our passion is to deliver inspired cabinetry solutions to suit all your needs, supported by our phenomenal star class customer service"
The website should convey quality and professionalism.
Thank you.
Target Market(s)
Homeowners/ Contractors
Industry/Entity Type
Entertainment
Coding
Coded - Design and coding required
Number of Pages Required
1 page
Look and feel
Each slider illustrates characteristics of the customer's brand and the style your logo design should communicate.

```html
<!DOCTYPE html>
<html lang="en">
<head>
<meta charset="utf-8">
<title>Brindlemoor Custom Cabinets — Home</title>
<link href="https://fonts.googleapis.com/css2?family=Arimo:wght@400;700&display=swap" rel="stylesheet">
<style>
  :root {
    --edge: #ffffff;
    --page: #cccccc;
    --header: #444444;
    --accent: #f15a22;
    --tab-line: #2a2a2a;
    --panel: #ffffff;
    --ink: #000000;
    --photo-warm: #8a6a48;
    --photo-cool: #c9c6c0;
  }
  * { box-sizing: border-box; margin: 0; padding: 0; }
  html, body { width: 1200px; height: 562px; overflow: hidden; }
  body {
    background: var(--edge);
    font-family: "Arimo", Arial, sans-serif;
    color: var(--ink);
    position: relative;
  }
  .site {
    position: absolute; left: 3px; top: 3px; width: 1197px; height: 559px;
    background: var(--page);
  }
  .site-header {
    position: absolute; left: 0; top: 0; width: 100%; height: 113px;
    background: var(--header);
  }
  .brand {
    position: absolute; left: 268px; top: 38px;
    display: flex; align-items: center; gap: 10px;
    color: var(--accent);
    font-weight: 700; font-size: 26px; letter-spacing: 0.5px;
  }
  .brand-mark { width: 22px; height: 22px; background: var(--accent); }
  .main-nav {
    position: absolute; left: 271px; top: 100px;
    display: flex; height: 26px;
  }
  .main-nav a {
    display: block; height: 26px; line-height: 26px;
    background: var(--accent); color: var(--ink);
    font-size: 11px; font-weight: 700; text-decoration: none;
    border-left: 1px solid var(--tab-line);
    text-align: center;
  }
  .main-nav a:last-child { border-right: 1px solid var(--tab-line); }
  .content {
    position: absolute; left: 255px; top: 132px; width: 697px; height: 359px;
    background: var(--panel);
    padding: 22px 10px 0 6px;
  }
  .content h1 { font-size: 21px; font-weight: 700; line-height: 26px; margin-bottom: 12px; }
  .feature-photo {
    float: right; width: 311px; height: 262px; margin: 2px 0 6px 6px;
    background: linear-gradient(160deg, var(--photo-cool) 0%, #e8e4dc 40%, var(--photo-warm) 100%);
  }
  .content p { font-size: 9.6px; line-height: 13px; margin-bottom: 8px; }
  .site-footer {
    position: absolute; left: 0; top: 498px; width: 100%; height: 61px;
    background: var(--accent);
  }
  .site-footer p {
    position: absolute; left: 261px; top: 18px;
    font-size: 9.6px; line-height: 13px;
  }
</style>
</head>
<body>
<div class="site">
  <header class="site-header">
    <div class="brand"><span class="brand-mark"></span><span class="brand-name">BRINDLEMOOR</span></div>
    <nav class="main-nav">
      <a href="#" style="width:52px">Home</a>
      <a href="#" style="width:68px">About Us</a>
      <a href="#" style="width:57px">Gallery</a>
      <a href="#" style="width:65px">Services</a>
      <a href="#" style="width:67px">Warranty</a>
      <a href="#" style="width:79px">Contact Us</a>
    </nav>
  </header>

  <main class="content">
    <h1>Home</h1>
    <div class="feature-photo" role="img" aria-label="Photo of a bright custom kitchen with white cabinets, a dark wood island and hardwood floors"></div>
    <p>Lorem ipsum dolor sit amet, consectetur adipiscing elit. Sed consequat massa at hendrerit rutrum. Donec tincidunt velit libero, sed venenatis mauris euismod quis. Interdum et malesuada fames ac ante ipsum primis in faucibus. Proin commodo ullamcorper ligula vitae pharetra. Nam rutrum ipsum et pulvinar lobortis. Vivamus luctus, tortor id vulputate tempus, justo neque egestas elit, vel dapibus massa magna sit amet sapien. Mauris dapibus pulvinar tincidunt. Nulla facilisi. Etiam eget mauris nec tellus finibus sodales eu et tortor. Nullam et magna mauris. Mauris quis ipsum arcu.</p>
    <p>Nullam vel hendrerit odio, sed porttitor metus. Ut sapien eros, mollis et felis quis, tempus tempus elit. Sed interdum facilisis erat sed varius. Suspendisse potenti. Vestibulum ante ipsum primis in faucibus orci luctus et ultrices posuere cubilia Curae; Etiam finibus, ante vel rutrum sagittis, est enim eleifend quam, nec mollis libero justo gravida ipsum. Nullam aliquam accumsan turpis nec vehicula. Nam sed arcu quis odio interdum varius quis vel augue. Phasellus faucibus sagittis tristique. Praesent venenatis hendrerit lectus, et tincidunt metus egestas a. Nam ut vehicula magna. Donec et lobortis mauris, at luctus sem. Sed suscipit augue ante, eget maximus est cursus eget.</p>
    <p>Cras pharetra nibh sem, non ultricies urna suscipit ut. Nunc non nulla vel nulla eleifend efficitur. Etiam bibendum mauris non sem commodo gravida. Suspendisse a vestibulum massa. Duis id scelerisque neque, vitae convallis nisl. Sed laoreet leo nec tempus fermentum. Nulla venenatis nulla diam, eget maximus orci viverra et. Duis eu felis et tellus egestas porttitor et vitae justo. Fusce in.</p>
  </main>

  <footer class="site-footer">
    <p>© 2015 Brindlemoor Custom Cabinets, all rights reserved</p>
  </footer>
</div>
</body>
</html>
```